Magazine ad for bridal boutique
The Ivory Latch
We need an amazing ad to catch the eye of the brides perusing through this magazine who are determining where they should do their bridal gown-shopping.
Unit Size: 1/6 Horizontal Non-bleed size: 4.625" X 2.25" PDF/X-1A format All fonts and images must be embedded. No native files. Ad must be formatted in process colors (i.e. CMYK) Max ink density is 300%. DPI: 200 and Line Screen: 133 Ad must be accompanied by an acceptable SWOP 3 certified proof. Crop and registration marks must be offset 12 points so as not to invade the live area. Do not set white to overprint.

```html
<!DOCTYPE html>
<html lang="en">
<head>
<meta charset="utf-8">
<title>The Ivory Latch – Magazine Ad</title>
<link href="https://fonts.googleapis.com/css2?family=Roboto+Condensed:wght@300;400&display=swap" rel="stylesheet">
<style>
  :root {
    --ink: #0b0b0b;
    --panel-top: #151515;
    --panel-mid: #1f1f1f;
    --text: #ffffff;
    --text-soft: #d6d6d6;
    --text-faint: #8a8a8a;
    --accent-green: #3f9a6e;
    --gown-light: #f3ebe1;
    --gown-mid: #dccdbb;
    --gown-shadow: #a89682;
    --skin: #d9a48c;
  }
  * { margin: 0; padding: 0; box-sizing: border-box; }
  html, body {
    width: 1200px; height: 583px; overflow: hidden;
    background: var(--ink);
  }
  .ad {
    position: relative;
    width: 1200px; height: 583px;
    overflow: hidden;
    background: linear-gradient(180deg, var(--panel-top), var(--panel-mid) 55%, var(--ink));
    font-family: "Roboto Condensed", "Arial Narrow", sans-serif;
    color: var(--text);
  }
  .hero-photo {
    position: absolute;
    left: 470px; top: 0;
    width: 730px; height: 583px;
    background:
      radial-gradient(ellipse at 70% 40%, var(--gown-light) 0%, var(--gown-mid) 45%, transparent 75%),
      radial-gradient(ellipse at 30% 88%, var(--skin) 0%, transparent 35%),
      linear-gradient(135deg, #6e5a4c 0%, var(--gown-shadow) 35%, var(--gown-mid) 70%, var(--gown-light) 100%);
    -webkit-mask-image: linear-gradient(90deg, transparent 0%, #000 22%);
            mask-image: linear-gradient(90deg, transparent 0%, #000 22%);
  }
  .info {
    position: absolute;
    left: 0; top: 0;
    width: 570px; height: 583px;
    text-align: center;
  }
  .brand { position: absolute; top: 62px; left: 0; width: 100%; }
  .brand-name {
    font-size: 44px; font-weight: 300; letter-spacing: 1px; line-height: 1;
  }
  .brand-city {
    margin-top: 6px;
    font-size: 13px; font-weight: 300; letter-spacing: 4px;
    color: var(--text-soft);
  }
  .headline {
    position: absolute; top: 170px; left: 0; width: 100%;
    font-size: 33px; font-weight: 400;
  }
  .appointment {
    position: absolute; top: 248px; left: 0; width: 100%;
    font-size: 22px; font-weight: 400; line-height: 1.4;
  }
  .address {
    position: absolute; top: 384px; left: 0; width: 100%;
    font-size: 19px; font-weight: 400; line-height: 1.55;
    color: var(--text-soft);
  }
  .marker {
    position: absolute; top: 470px; left: 50%;
    width: 22px; height: 22px; margin-left: -11px;
    border-radius: 50%;
    background: var(--accent-green);
  }
  .website {
    position: absolute; top: 508px; left: 0; width: 100%;
    font-size: 18px; font-weight: 400;
  }
  .credit {
    position: absolute; top: 552px; left: 0; width: 100%;
    font-size: 10px; font-weight: 300;
    color: var(--text-faint);
  }
</style>
</head>
<body>
  <div class="ad">
    <div class="hero-photo" role="img" aria-label="Close-up photograph of a bride in an ivory lace gown with floral beading, holding a long strand of pearls"></div>

    <div class="info">
      <div class="brand">
        <div class="brand-name">The Ivory Latch</div>
        <div class="brand-city">NEW YORK</div>
      </div>

      <p class="headline">Bridal gowns Upto 75% off Retail</p>

      <p class="appointment">By Appointment Only<br>212.555.0148</p>

      <p class="address">118 W. 19th St. Suite 402<br>New York, NY 10011</p>

      <span class="marker" aria-hidden="true"></span>

      <p class="website">www.ivorylatch.org</p>

      <p class="credit">Photographs by Dana Morrow Photography</p>
    </div>
  </div>
</body>
</html>
```